Email Banner for Technology Company

We need a new email banner. The purpose of the email banner is to make us look more professional as a business and keep all communications with clients uniform. The previous designs which we have included below have now become outdated as our brand has developed and we need the new banner to become more aligned and modern.

We are a marketing organization that specialises in lead generation, email newsletters are sent to prospects on a regular basis. Therefore, it is important that we have an aesthetically pleasing banner as this is the first real impression prospects have our business. First impressions matter.

We are looking for a new email banner design as the current design is now outdated and does not reflect who we are as a business.

The new banners are required for launch at the start of Q2.

There is future work in the pipeline for the winning design. We have multiple industry sites that will require the new design as well as creating each of these in multiple languages.

The design must include the Zevomarkly wording the tagline 'The Ultimate Research Library for Technology Pro's.
It needs to be creative and fun but still remain professional, sticking with the colour theme that already exists.

Requirements
Must have
• The design must include the Zevomarkly wording the tagline 'The Ultimate Research Library for Technology Pro's.

```html
<!DOCTYPE html>
<html lang="en">
<head>
<meta charset="utf-8">
<title>Zevomarkly Email Banner</title>
<link rel="stylesheet" href="https://fonts.googleapis.com/css2?family=PT+Sans:wght@700&display=swap">
<style>
  :root {
    --sky-light: #d9f1fb;
    --sky-mid: #bfe8f8;
    --sky-soft: #cdeefa;
    --brand-blue: #0aa6e5;
    --button-blue: #5ccaf2;
    --button-edge: #1aaee6;
    --white: #ffffff;
    --target-light: #e8f6fc;
    --target-mid: #7fd3f3;
  }
  html, body {
    margin: 0;
    padding: 0;
    overflow: hidden;
  }
  body {
    width: 1200px;
    height: 180px;
  }
  .banner {
    position: relative;
    width: 1200px;
    height: 180px;
    overflow: hidden;
    background: linear-gradient(100deg, var(--sky-light) 0%, var(--sky-mid) 45%, var(--sky-soft) 75%, var(--sky-light) 100%);
    font-family: "PT Sans", "Myriad Pro", sans-serif;
  }
  .brand-name {
    position: absolute;
    left: 14px;
    top: 46px;
    margin: 0;
    font-size: 62px;
    font-weight: 700;
    line-height: 1;
    letter-spacing: -0.5px;
    color: var(--brand-blue);
  }
  .tagline {
    position: absolute;
    left: 372px;
    top: 58px;
    margin: 0;
    font-size: 24.5px;
    font-weight: 700;
    line-height: 1;
    color: var(--brand-blue);
    white-space: nowrap;
  }
  .cta-button {
    position: absolute;
    left: 588px;
    top: 99px;
    width: 114px;
    height: 28px;
    border-radius: 6px;
    background: var(--button-blue);
    box-shadow: 1px 2px 0 var(--button-edge);
    color: var(--white);
    font-size: 20px;
    font-weight: 700;
    line-height: 28px;
    text-align: center;
    text-decoration: none;
  }
  .target-illustration {
    position: absolute;
    left: 1003px;
    top: 5px;
    width: 192px;
    height: 173px;
    border-radius: 48% 48% 40% 40%;
    background: radial-gradient(ellipse at 60% 40%, var(--white) 0%, var(--target-light) 40%, var(--target-mid) 100%);
  }
</style>
</head>
<body>
  <div class="banner">
    <p class="brand-name">Zevomarkly</p>
    <p class="tagline">The Ultimate Research Library for Technology Pro's</p>
    <a class="cta-button" href="#">Click Here</a>
    <div class="target-illustration" role="img" aria-label="Illustration of a dartboard target on a stand with darts hitting the bullseye and lying on the ground"></div>
  </div>
</body>
</html>
```